Web Design for couples website

About us:
Duoglimmer.sg is a new startup website that aims to suggest and promote activities for young couples. The site will feature a blog and a group deals page (i.e Bulkaro).

What we need:
We require a talented designer to design a theme for the website. The design must include at least the following:
1. Logo Design - A logo should be provided along with the website design. The design should match the overall design of the website (or vice versa). The logo should include the words "Duoglimmer.sg" or "Duoglimmer". Capitalisation of the alphabets are not critical.

2 - Home / Landing page
The layout of this page should be similar to the standard 2 / 3 column quillpress pages with an image slider on top to feature articles / deals. There should also be a column on the side to include widgets such as social networking and mailing list subscription, etc

3. Deals Listing Page
This page will have a listing of all current group deals, similar to that of Bulkaro. The layout can either have deals listed in 1 or 2 columns.

4. Past Deals Page - See references below

5. Deal Page
Detailed information page for each specific deal. This should include deal image, title, buy button, timer, social media buttons, two column text.

References for deal pages:
www.ventopik.com.sg
http://www.plumvoucher.com.au/daily-offers
www.tarnibuyasia.com
www.frolmart.com

6. General page design for miscellaneous pages like "About", "Contact", etc.

The overall theme of the website should cater to an audience of 18-30 year old young adults. Preferably to have something less colourful and give the overall feel of class. This should cater generally to females but males as well, so less (or no)pink / red would be preferable. But don't let yourself get restricted by these requirements and feel free to let your creative juices flow!
Updates

Hi Designers,

Thank you for your submissions so far. I would like to point out that the deal listing page will only be a sub section of the page.  Would appreciate if priority was given to the main / landing page slider and 2 or 3 columns for articles below.

Other priority would be for the single deal design, where I'm more interested to have more unique buttons such as "buy now" and "time left" .

Also to note, only .PSD design file is required. No coding (HTML / CSS) is necessary and should also be friendly for developers to work with.

Hi Designers,

 
Please submit proposal designs based on requirements on landing page or deal listings page as these would be my main requirements for consideration.

Also, Do try to keep the theme clean and easy on the eyes. Overall, I'm looking for something that is simplistic and/or classy with elegance.

Target Market(s)

18 - 30 years old young adults interested in dating and activities for couples

Industry/Entity Type

Media

Requirements
Must have
• - Logo
- Home
- Deal Page (specific)
- General layout

```html
<!DOCTYPE html>
<html lang="en">
<head>
<meta charset="utf-8">
<title>Duoglimmer.sg — Home</title>
<link rel="stylesheet" href="https://fonts.googleapis.com/css2?family=Crimson+Pro:wght@400;600;700&family=Arimo:wght@400&display=swap">
<style>
  :root {
    --page-top: #ebe7f0;
    --page-bottom: #ffffff;
    --brand-plum: #5b2b4f;
    --nav-text: #5b2b4f;
    --nav-frame: #2f2a3d;
    --nav-fill: #dcd4e6;
    --nav-edge: #b3a6c6;
    --nav-divider: #a99bbd;
    --slider-frame: #b4a6c4;
    --photo-top: #9fa9b8;
    --photo-bottom: #3b3a40;
    --caption-band: rgba(50, 48, 56, 0.72);
    --contact-fill: #cfc5db;
    --input-fill: #fbfafc;
    --panel-top: #e4e2e7;
    --panel-bottom: #f6f5f7;
    --footer-band: #e5dfec;
    --bullet: #a99bbd;
    --ink: #1d1b22;
    --social-dark: #4b4660;
    --social-light: #7d7598;
    --text-serif: "Crimson Pro", Georgia, serif;
    --text-sans: "Arimo", Arial, sans-serif;
  }
  * { box-sizing: border-box; margin: 0; padding: 0; }
  html, body { width: 1200px; height: 1000px; overflow: hidden; }
  body {
    position: relative;
    background: linear-gradient(var(--page-top) 0%, #f3f0f6 60%, var(--page-bottom) 100%);
    font-family: var(--text-serif);
    color: var(--ink);
  }
  .abs { position: absolute; }

  .brand-name { color: var(--brand-plum); font-family: var(--text-serif); font-weight: 700; white-space: nowrap; }
  .site-logo { left: 120px; top: 9px; font-size: 42px; line-height: 52px; }
  .call-line { right: 118px; top: 14px; font-size: 22px; font-weight: 700; line-height: 28px; }

  .main-nav {
    left: 122px; top: 107px; width: 956px; height: 50px;
    border: 5px solid var(--nav-frame);
    background: radial-gradient(ellipse at center, var(--nav-fill) 70%, var(--nav-edge) 100%);
    display: flex; align-items: center;
  }
  .nav-item {
    height: 100%; display: flex; align-items: center; justify-content: center;
    color: var(--nav-text); font-size: 18px; letter-spacing: 0.3px;
    border-right: 2px solid var(--nav-divider);
  }
  .nav-item:last-child { border-right: none; }
  .nav-item.is-current span { background: #fff; padding: 0 16px; line-height: 24px; font-weight: 700; }

  .hero-slider { left: 122px; top: 170px; width: 664px; height: 330px; background: var(--slider-frame); }
  .hero-photo {
    left: 6px; top: 6px; width: 649px; height: 318px;
    background: linear-gradient(var(--photo-top), #6f7079 55%, var(--photo-bottom));
  }
  .hero-caption { left: 6px; top: 215px; width: 649px; height: 109px; background: var(--caption-band); color: #fff; font-family: var(--text-sans); }
  .hero-title { position: absolute; left: 6px; top: 12px; font-size: 22px; }
  .hero-text { position: absolute; left: 8px; top: 51px; font-size: 13px; line-height: 18px; width: 630px; }

  .quick-contact { left: 794px; top: 168px; width: 280px; height: 332px; background: var(--contact-fill); }
  .quick-contact h2 { position: absolute; left: 10px; top: 0; font-size: 34px; line-height: 40px; color: var(--brand-plum); font-weight: 700; }
  .field-label { position: absolute; font-size: 20px; line-height: 24px; }
  .field-input { position: absolute; width: 203px; height: 34px; background: var(--input-fill); border: 1px solid var(--nav-frame); }

  .submit-button {
    left: 874px; top: 518px; width: 139px; height: 41px;
    border: 4px solid var(--nav-frame);
    background: radial-gradient(ellipse at center, #b9a9cc 40%, #7c6a95 100%);
    color: #fff; font-size: 22px; text-align: center; line-height: 33px; letter-spacing: 0.5px;
  }

  .welcome { left: 120px; top: 517px; font-size: 30px; line-height: 50px; white-space: nowrap; }
  .welcome .brand-name { font-size: 42px; margin-left: 6px; vertical-align: -2px; }

  .article-panel { background: linear-gradient(var(--panel-top), var(--panel-bottom)); box-shadow: 6px 2px 0 #f8f8f8; }
  .panel-title { position: absolute; color: var(--brand-plum); font-size: 18px; }
  .panel-text { position: absolute; font-family: var(--text-sans); font-size: 11px; line-height: 13px; white-space: pre; }

  .footer-band { left: 120px; top: 852px; width: 963px; height: 95px; background: var(--footer-band); }
  .reference-link { position: absolute; left: 32px; top: 22px; font-size: 13px; }
  .social-link { position: absolute; top: 17px; width: 28px; height: 28px; background: var(--social-dark); border-radius: 3px; }

  .footer-nav { right: 117px; top: 956px; font-size: 11px; color: var(--nav-text); white-space: nowrap; }
  .footer-nav .dot { color: var(--bullet); margin: 0 2px; }
  .footer-nav .is-current { font-weight: 700; }
  .copyright { right: 117px; top: 972px; font-size: 9.5px; font-weight: 700; }
</style>
</head>
<body>
  <header>
    <div class="abs site-logo brand-name">Duoglimmer.sg</div>
    <div class="abs call-line">call us now : 000-000-0000</div>
  </header>

  <nav class="abs main-nav">
    <div class="nav-item is-current" style="width:111px"><span>HOME</span></div>
    <div class="nav-item" style="width:228px">DEALS PAGE LISTING</div>
    <div class="nav-item" style="width:235px">DEAL PAGE SPECIFIC</div>
    <div class="nav-item" style="width:161px">ABOUT US</div>
    <div class="nav-item" style="flex:1">CONTACT US</div>
  </nav>

  <section class="abs hero-slider">
    <div class="abs hero-photo" role="img" aria-label="Photo of a group of young friends jumping in the air under a cloudy sky"></div>
    <div class="abs hero-caption">
      <div class="hero-title">Punch Line Goes to here</div>
      <p class="hero-text">Sample text here sample Sample text here sample Sample text here sample Sample text here sample Sample text here sample Sample text here sample Sample text here sample Sample text here sample</p>
    </div>
  </section>

  <aside class="abs quick-contact">
    <h2>Quick Contact</h2>
    <div class="field-label" style="left:17px;top:45px">First Name :</div>
    <div class="field-input" style="left:14px;top:77px"></div>
    <div class="field-label" style="left:22px;top:122px">Company Name :</div>
    <div class="field-input" style="left:16px;top:153px"></div>
    <div class="field-label" style="left:30px;top:194px">Email :</div>
    <div class="field-input" style="left:16px;top:225px"></div>
    <div class="field-label" style="left:33px;top:267px">Phone :</div>
    <div class="field-input" style="left:16px;top:291px"></div>
  </aside>
  <div class="abs submit-button">SUBMIT</div>

  <div class="abs welcome">Welcome to <span class="brand-name">Duoglimmer.sg</span></div>

  <section class="abs article-panel" style="left:115px;top:589px;width:952px;height:104px">
    <div class="panel-title" style="left:13px;top:9px">Punch line gose to heare</div>
    <div class="panel-text" style="left:11px;top:57px">sample text   sample text
sample text</div>
    <div class="panel-text" style="left:499px;top:53px">sample text    sample text
sample text    sample taxt</div>
  </section>

  <section class="abs article-panel" style="left:119px;top:706px;width:472px;height:127px">
    <div class="panel-title" style="left:17px;top:8px">Punch line gose to heare</div>
    <div class="panel-text" style="left:9px;top:64px">sample text    sample text
sample text    sample taxt</div>
  </section>

  <section class="abs article-panel" style="left:603px;top:705px;width:472px;height:125px">
    <div class="panel-title" style="left:9px;top:9px">Punch line gose to heare</div>
    <div class="panel-text" style="left:39px;top:57px;font-size:12px;line-height:14px">sample text    sample text
sample text    sample taxt</div>
  </section>

  <footer>
    <div class="abs footer-band">
      <div class="reference-link">Reference  Link</div>
      <div class="social-link" style="left:766px" aria-label="Social network link"></div>
      <div class="social-link" style="left:807px" aria-label="Social network link"></div>
      <div class="social-link" style="left:847px;background:var(--social-light)" aria-label="Social network link"></div>
    </div>
    <div class="abs footer-nav"><span class="dot">●</span><span class="is-current">HOME</span> <span class="dot">●</span>DEALS PAGE LISTING <span class="dot">●</span>DEAL PAGE SPECIFIC <span class="dot">●</span>ABOUT US <span class="dot">●</span>CONTACT US</div>
    <div class="abs copyright">copyright 2012 by Duoglimmer.sg all rights reseeved.</div>
  </footer>
</body>
</html>
```